Author needs cover design for health related book

I need the front cover designed for an upcoming book. I want a cover that will stand out when viewed in a thumbnail on sites such as Brindleway. I'm open to the color scheme. The cover design should convey hopeful, uplifting energy, trust, and confidence. Nothing cute or frilly, please. The book is written for newly diagnosed cancer patients. The book title is: They Told Me Today, So What Next? Subtitle: Bravely Facing Cancer Through Worry, Confusion and Dread
Author: Darlisse Hovard
I'm not window shopping. I will definitely pick one of the submitted designs.
Target Market(s)
Newly diagnosed cancer patients
Industry/Entity Type
Health Care
Look and feel
Each slider illustrates characteristics of the customer's brand and the style your logo design should communicate.

```html
<!DOCTYPE html>
<html lang="en">
<head>
<meta charset="utf-8">
<title>They Told Me Today, So What Next? — Book Cover</title>
<link href="https://fonts.googleapis.com/css2?family=Tinos:wght@400;700&display=swap" rel="stylesheet">
<style>
  :root {
    --page-bg: #eeeceb;
    --cover-bg: #ffffff;
    --ink: #141414;
    --ink-soft: #4a4a4a;
    --accent-red: #d5222b;
    --rule: #555555;
    --gold-light: #fbe13c;
    --gold-mid: #f2c526;
    --gold-deep: #e3a51a;
    --sky-light: #fbf3e6;
    --sun-glow: #f6c98a;
    --dusk: #d59a62;
    --foliage: #4f4a26;
    --foliage-dark: #2c2a14;
  }
  * { margin: 0; padding: 0; box-sizing: border-box; }
  html, body {
    width: 1022px; height: 1200px; overflow: hidden;
    background: var(--page-bg);
  }
  .canvas {
    position: relative; width: 1022px; height: 1200px;
    display: flex; justify-content: center;
  }
  .cover {
    position: relative; width: 800px; height: 1200px;
    background: var(--cover-bg);
    font-family: 'Tinos', 'Times New Roman', serif;
    overflow: hidden;
  }
  .title-line {
    position: absolute; left: 0; width: 100%;
    text-align: center; white-space: nowrap;
    line-height: 1; text-transform: uppercase;
  }
  .title-top {
    top: 86px; font-size: 80px; font-weight: 400;
    color: var(--ink); letter-spacing: 1px;
  }
  .title-accent {
    top: 172px; font-size: 110px; font-weight: 700;
    color: var(--accent-red); letter-spacing: 1px;
  }
  .title-bottom {
    top: 290px; font-size: 80px; font-weight: 400;
    color: var(--ink); letter-spacing: 1px;
  }
  .divider {
    position: absolute; left: 90px; width: 620px; height: 14px;
  }
  .divider-top { top: 412px; }
  .divider-bottom { top: 592px; }
  .subtitle {
    position: absolute; top: 440px; left: 0; width: 100%;
    text-align: center; text-transform: uppercase;
    font-size: 37px; line-height: 47px; color: var(--ink);
  }
  .hero-photo {
    position: absolute; top: 644px; left: 0; width: 800px; height: 444px;
    background:
      radial-gradient(ellipse 300px 200px at 420px 250px, var(--sun-glow) 0%, rgba(246,201,138,0) 70%),
      linear-gradient(180deg, var(--cover-bg) 0%, var(--sky-light) 25%, var(--sun-glow) 55%, var(--dusk) 68%, var(--foliage) 82%, var(--foliage-dark) 100%);
  }
  .author-band {
    position: absolute; top: 1088px; left: 0; width: 800px; height: 112px;
    background: linear-gradient(90deg, var(--gold-light) 0%, var(--gold-mid) 55%, var(--gold-deep) 100%);
    display: flex; align-items: center; justify-content: center;
  }
  .author-name {
    font-size: 54px; font-weight: 400; color: var(--accent-red);
    text-transform: uppercase; letter-spacing: 1px; line-height: 1;
  }
</style>
</head>
<body>
<div class="canvas">
  <main class="cover">
    <h1 class="book-title">
      <span class="title-line title-top">They Told Me</span>
      <span class="title-line title-accent">Today,</span>
      <span class="title-line title-bottom">So What Next?</span>
    </h1>

    <svg class="divider divider-top" viewBox="0 0 620 14" aria-hidden="true">
      <line x1="0" y1="7" x2="300" y2="7" stroke="var(--rule)" stroke-width="1.5"/>
      <line x1="320" y1="7" x2="620" y2="7" stroke="var(--rule)" stroke-width="1.5"/>
      <rect x="304" y="1" width="9" height="9" fill="var(--accent-red)" transform="rotate(45 310 7)"/>
    </svg>

    <p class="subtitle">Bravely Facing Cancer<br>Through Worry, Confusion<br>and Dread</p>

    <svg class="divider divider-bottom" viewBox="0 0 620 14" aria-hidden="true">
      <line x1="0" y1="7" x2="300" y2="7" stroke="var(--rule)" stroke-width="1.5"/>
      <line x1="320" y1="7" x2="620" y2="7" stroke="var(--rule)" stroke-width="1.5"/>
      <rect x="304" y="1" width="9" height="9" fill="var(--accent-red)" transform="rotate(45 310 7)"/>
    </svg>

    <div class="hero-photo" role="img" aria-label="Photo of a woman with arms outstretched and eyes closed, facing a glowing sunset above a line of trees"></div>

    <footer class="author-band">
      <span class="author-name">Darlisse Hovard</span>
    </footer>
  </main>
</div>
</body>
</html>
```